Trendy eye catching business card for lawn mowing business

Verge Kings, a local community lawn mowing service, requires an eye catching trendy business card to drop into letterboxes.

We could simply throw something together from a Microsoft Word template, but we are wanting something more than this. Some other business’ images are attached for some inspiration.

We are requiring the card to have Verge Kings with our slogan, Call The Pembrys. In addition, provide details with that we are a local, affordable lawn mowing service, and for other gardening matters to simply just ask!
Plus the relevant contact details, phone, email, social media.

Target Market(s)

Local community members who require assistance with their garden care

Industry/Entity Type

Gardening

Contact Information for Business Card

the name VERGE KINGS is our logo
telephone logo 0438 215 967
email logo vergekings@postbox-demo.com
Instagram logo vergekings
Facebook logo vergekings.sth
Lawn Mowing Service
Local Affordable
edge trim, blow and clipping removal included.
Other gardening matters, just ask!

Font styles to use
Serif
Sans Serif
Decorative
Script

Colors
9bcb3c
ffffff

Requirements
Must have
• All the details listed in Business Card Details.
Make these words prominent:
Verge Kings
Lawn Mowing Service
Local
Affordable
Nice to have
• Our slogan ‘Call The Pembrys’ incorporated.
Different colour background for front and reverse side
Greens, white and black colours
Subtle grass blades images incorporated
Should not have
• No images of lawnmowers.
No images of men/cartoons.
No using initials for Verge Kings

```html
<!DOCTYPE html>
<html lang="en">
<head>
<meta charset="utf-8">
<title>Verge Kings – Business Card</title>
<link rel="stylesheet" href="https://fonts.googleapis.com/css2?family=Montserrat:wght@400;500;600;700&family=Playfair+Display:wght@700;800&display=swap">
<style>
  :root{
    --stage:#3a3d41;
    --charcoal:#25282b;
    --lime:#9bcb3c;
    --white:#ffffff;
    --ink-soft:#e6e8ea;
  }
  *{box-sizing:border-box;margin:0;padding:0}
  html,body{width:1200px;height:900px;overflow:hidden}
  body{background:var(--stage);position:relative;font-family:"Montserrat",sans-serif}

  .card{position:absolute;width:640px;height:366px;overflow:hidden;box-shadow:0 14px 34px rgba(0,0,0,.35)}

  /* Service side */
  .card--service{left:500px;top:60px;background:var(--charcoal)}
  .service__band-top{position:absolute;left:0;top:0;width:100%;height:16px;background:var(--lime)}
  .service__band-bottom{position:absolute;left:0;bottom:0;width:100%;height:58px;background:var(--lime)}
  .service__brand{position:absolute;right:54px;top:62px;display:flex;align-items:center;gap:14px}
  .service__brand-dot{width:22px;height:22px;border-radius:50%;background:var(--white)}
  .brand-block{display:flex;flex-direction:column;align-items:flex-start}
  .brand-name{font-weight:700;font-size:34px;letter-spacing:.5px;line-height:1}
  .brand-slogan{font-weight:500;font-size:11px;letter-spacing:2px;margin-top:6px;text-transform:uppercase}
  .service__brand .brand-name,.service__brand .brand-slogan{color:var(--white)}
  .service__copy{position:absolute;left:38px;top:160px;border-left:4px solid var(--lime);padding-left:16px}
  .service__title{font-family:"Playfair Display",serif;font-weight:800;font-size:34px;line-height:1.1;color:var(--white)}
  .service__title .accent{color:var(--lime)}
  .service__text{margin-top:10px;font-size:14px;line-height:1.45;color:var(--ink-soft);max-width:520px}

  /* Contact side */
  .card--contact{left:60px;top:470px;background:var(--white)}
  .contact__strip{position:absolute;left:0;top:30px;width:370px;height:8px;background:var(--lime)}
  .contact__panel{position:absolute;left:0;top:38px;width:370px;height:328px;background:var(--charcoal)}
  .contact__person{position:absolute;right:28px;top:24px;text-align:right}
  .contact__name{font-weight:600;font-size:30px;letter-spacing:.5px;color:var(--white);line-height:1}
  .contact__name .accent{color:var(--lime)}
  .contact__role{font-size:14px;color:var(--ink-soft);margin-top:6px}
  .contact__list{position:absolute;left:0;top:118px;width:430px;list-style:none}
  .contact__item{display:flex;align-items:center;justify-content:flex-end;height:46px;margin-bottom:5px}
  .contact__text{font-size:15px;color:var(--ink-soft);margin-right:14px;width:300px;text-align:right}
  .contact__icon{width:62px;height:46px;background:var(--lime);border-radius:10px;display:flex;align-items:center;justify-content:center}
  .contact__icon svg{width:24px;height:24px}
  .contact__brand{position:absolute;left:450px;top:150px;width:170px;display:flex;align-items:center;gap:10px}
  .contact__brand-dot{width:16px;height:16px;border-radius:50%;background:var(--lime);flex:none}
  .contact__brand .brand-name{font-size:24px;color:var(--lime)}
  .contact__brand .brand-slogan{font-size:8px;letter-spacing:1.4px;color:var(--lime)}
</style>
</head>
<body>

<section class="card card--service" aria-label="Business card, service side">
  <div class="service__band-top"></div>
  <div class="service__brand">
    <span class="service__brand-dot"></span>
    <div class="brand-block">
      <span class="brand-name">Verge Kings</span>
      <span class="brand-slogan">Call The Pembrys</span>
    </div>
  </div>
  <div class="service__copy">
    <h1 class="service__title"><span class="accent">Lawn Mowing</span> Service:</h1>
    <p class="service__text">Local Affordable, edge trim, blow and clipping removal included. Other gardening matters, just ask!</p>
  </div>
  <div class="service__band-bottom"></div>
</section>

<section class="card card--contact" aria-label="Business card, contact side">
  <div class="contact__strip"></div>
  <div class="contact__panel">
    <div class="contact__person">
      <h2 class="contact__name">DALE <span class="accent">FENWICK</span></h2>
      <p class="contact__role">Managing Director</p>
    </div>
  </div>
  <ul class="contact__list">
    <li class="contact__item">
      <span class="contact__text">0438 215 967</span>
      <span class="contact__icon">
        <svg viewBox="0 0 24 24" fill="none" stroke="#fff" stroke-width="1.8"><circle cx="12" cy="12" r="10"/><path d="M9 7.5l1.5 2.5-1 1.2a6 6 0 0 0 3.3 3.3l1.2-1 2.5 1.5-.8 1.6c-3.8.2-8-4-7.8-7.8z" stroke-linejoin="round"/></svg>
      </span>
    </li>
    <li class="contact__item">
      <span class="contact__text">vergekings@postbox-demo.com</span>
      <span class="contact__icon">
        <svg viewBox="0 0 24 24" fill="none" stroke="#fff" stroke-width="1.8"><circle cx="12" cy="12" r="10"/><rect x="7" y="8.5" width="10" height="7" rx="1"/><path d="M7 9l5 4 5-4"/></svg>
      </span>
    </li>
    <li class="contact__item">
      <span class="contact__text">vergekings</span>
      <span class="contact__icon">
        <svg viewBox="0 0 24 24" fill="none" stroke="#fff" stroke-width="1.8"><circle cx="12" cy="12" r="9"/></svg>
      </span>
    </li>
    <li class="contact__item">
      <span class="contact__text">vergekings.sth</span>
      <span class="contact__icon">
        <svg viewBox="0 0 24 24" fill="none" stroke="#fff" stroke-width="1.8"><rect x="4" y="4" width="16" height="16" rx="3"/></svg>
      </span>
    </li>
  </ul>
  <div class="contact__brand">
    <span class="contact__brand-dot"></span>
    <div class="brand-block">
      <span class="brand-name">Verge Kings</span>
      <span class="brand-slogan">Call The Pembrys</span>
    </div>
  </div>
</section>

</body>
</html>
```